Quillbrook Pawn Shop Moving

My pawn shop will be relocating on August 1st 2012. We are moving 1 block north at the corner of Drayford and Kettner Ave. Next to Brisko. The new location will include bigger facilities and shopping area. The new address is 2481 N Drayford Rd, Westmoreland, IL 60917 708-555-GOLD (4653). I would like to see a neon light border, with dollar symbols at each corner. I would also like to print 2 per page, so thinking 8.5 x 5.5 with the design running horizontal.

```html
<!DOCTYPE html>
<html lang="en">
<head>
<meta charset="utf-8">
<title>Quillbrook Pawn Shop – We Are Moving</title>
<link rel="stylesheet" href="https://fonts.googleapis.com/css2?family=Saira:wght@300;400;600;700&display=swap">
<style>
  :root {
    --bg: #000000;
    --wall-warm: #4a2a26;
    --wall-dark: #0c0807;
    --neon-green: #5cf08a;
    --neon-green-core: #e6ffe9;
    --neon-red: #ff3b3b;
    --neon-red-core: #ffe0dc;
    --neon-white: #f4f4f4;
    --lime-light: #c3f59a;
    --lime: #95e873;
    --neon-yellow: #f3f23c;
  }
  html, body {
    margin: 0;
    padding: 0;
    width: 1200px;
    height: 776px;
    overflow: hidden;
    background: var(--bg);
  }
  .flyer {
    display: block;
    width: 1200px;
    height: 776px;
    font-family: "Saira", sans-serif;
  }
  .neon-frame {
    fill: none;
    stroke: var(--neon-green-core);
    stroke-width: 4;
    filter: drop-shadow(0 0 4px var(--neon-green)) drop-shadow(0 0 10px var(--neon-green));
  }
  .neon-frame--outer { stroke: var(--neon-green); stroke-width: 6; }
  .dollar {
    font-family: "Saira", sans-serif;
    font-weight: 600;
    font-size: 140px;
    fill: var(--neon-green-core);
    stroke: var(--neon-green);
    stroke-width: 3;
    filter: drop-shadow(0 0 6px var(--neon-green)) drop-shadow(0 0 14px var(--neon-green));
  }
  .headline {
    font-weight: 700;
    font-size: 98px;
    fill: #ffffff;
    stroke: var(--neon-green);
    stroke-width: 2;
    filter: drop-shadow(0 0 6px var(--neon-green)) drop-shadow(0 0 12px var(--neon-green));
  }
  .shop-name {
    font-weight: 300;
    font-size: 124px;
    fill: var(--neon-red-core);
    stroke: var(--neon-red);
    stroke-width: 3;
    filter: drop-shadow(0 0 6px var(--neon-red)) drop-shadow(0 0 14px var(--neon-red));
  }
  .shop-type {
    font-weight: 400;
    font-size: 94px;
    fill: var(--neon-white);
    filter: drop-shadow(0 0 6px rgba(255,255,255,.7));
  }
  .location {
    font-weight: 400;
    font-size: 54px;
    fill: var(--lime-light);
    filter: drop-shadow(0 0 5px var(--lime));
  }
  .address {
    font-weight: 400;
    font-size: 42px;
    fill: var(--lime);
    filter: drop-shadow(0 0 5px var(--lime));
  }
  .phone {
    font-weight: 400;
    font-size: 106px;
    fill: var(--neon-yellow);
    filter: drop-shadow(0 0 6px var(--neon-yellow)) drop-shadow(0 0 12px rgba(243,242,60,.6));
  }
</style>
</head>
<body>
<svg class="flyer" viewBox="0 0 1200 776" xmlns="http://www.w3.org/2000/svg">
  <defs>
    <radialGradient id="wall-glow" cx="50%" cy="48%" r="60%">
      <stop offset="0%" stop-color="var(--wall-warm)"/>
      <stop offset="55%" stop-color="#2a1816"/>
      <stop offset="100%" stop-color="var(--wall-dark)"/>
    </radialGradient>
  </defs>

  <rect class="backdrop" width="1200" height="776" fill="var(--bg)"/>
  <rect class="brick-wall" x="80" y="90" width="1040" height="610" fill="url(#wall-glow)"
        role="img" aria-label="Dimly lit red brick wall behind the neon signage"/>

  <g class="border">
    <line class="neon-frame neon-frame--outer" x1="112" y1="72" x2="1088" y2="72"/>
    <line class="neon-frame" x1="112" y1="86" x2="1088" y2="86"/>
    <line class="neon-frame neon-frame--outer" x1="112" y1="732" x2="1088" y2="732"/>
    <line class="neon-frame" x1="112" y1="718" x2="1088" y2="718"/>
    <line class="neon-frame neon-frame--outer" x1="40" y1="170" x2="40" y2="610"/>
    <line class="neon-frame" x1="54" y1="170" x2="54" y2="610"/>
    <line class="neon-frame neon-frame--outer" x1="1160" y1="170" x2="1160" y2="610"/>
    <line class="neon-frame" x1="1146" y1="170" x2="1146" y2="610"/>
  </g>

  <g class="corners" text-anchor="middle">
    <text class="dollar" x="58" y="150">$</text>
    <text class="dollar" x="1142" y="150">$</text>
    <text class="dollar" x="58" y="730">$</text>
    <text class="dollar" x="1142" y="730">$</text>
  </g>

  <g class="headline-box">
    <rect class="neon-frame neon-frame--outer" x="146" y="22" width="916" height="168" rx="30"/>
    <rect class="neon-frame" x="162" y="38" width="884" height="136" rx="22"/>
    <text class="headline" x="604" y="142" text-anchor="middle" textLength="810" lengthAdjust="spacingAndGlyphs">WE ARE MOVING</text>
  </g>

  <g class="details" text-anchor="middle">
    <text class="shop-name" x="606" y="318" textLength="910" lengthAdjust="spacing">QUILLBROOK</text>
    <text class="shop-type" x="606" y="426" textLength="600" lengthAdjust="spacingAndGlyphs">PAWN SHOP</text>
    <text class="location" x="609" y="502" textLength="942" lengthAdjust="spacingAndGlyphs">Corner of Drayford and Kettner Ave</text>
    <text class="address" x="609" y="558" textLength="942" lengthAdjust="spacingAndGlyphs">2481 N Drayford Rd, Westmoreland, IL 60917</text>
    <text class="phone" x="603" y="672" textLength="810" lengthAdjust="spacingAndGlyphs">708-555-GOLD</text>
  </g>
</svg>
</body>
</html>
```